Golden Era Hollywood Movie Poster Design for a Wedding Invitation

We're looking for a movie poster designed along the lines of the styles of posters in the included "posters" file. We're thinking the "title" of the "movie" should be "The Wedding of the Year". This will be for a wedding invitation to the wedding of "Marla Quenstedder" and "Daniel Fenwoller", so their names should be featured as the "stars" of the movie. The wedding will take place at Pell Arrow Studios in Hollywood, so you can put on the poster "Presented by Pell Arrow Studios". The other uploaded files are photos of the bride and groom. You don't need to use any of the poses in those photos - we'd like to have a pose that's along the lines of the examples in the "posters" file - but I included the photos of the bride and groom as references to help you make the final poster look like them (but in the style of an old Hollywood movie poster). Make them look beautiful and glamorous like stars in a movie from Hollywood's golden era. :)

Reason: The designs we've received so far aren't quite giving exactly the old-Hollywood feel we're looking for, so we're giving one 5-day extension to see additional designs.

```html
<!DOCTYPE html>
<html lang="en">
<head>
<meta charset="UTF-8">
<title>The Wedding of the Year</title>
<link rel="stylesheet" href="https://fonts.googleapis.com/css2?family=Yellowtail&family=Kaushan+Script&display=swap">
<style>
  :root {
    --frame: #3b3631;
    --sky: #2f8fc4;
    --sky-deep: #1f6f9f;
    --sun-red: #e0262a;
    --sun-deep: #a9151c;
    --gold: #f6b632;
    --gold-deep: #d99419;
    --title: #f4b63a;
    --ink: #2a2522;
    --stroke-blue: #3fa9e0;
    --photo-couple: #6b5a52;
    --photo-bride: #4f8fbf;
  }
  * { margin: 0; padding: 0; box-sizing: border-box; }
  html, body { width: 811px; height: 1200px; overflow: hidden; background: #ffffff; }
  .poster {
    position: relative;
    width: 811px;
    height: 1200px;
    background: var(--frame);
    padding: 12px;
    overflow: hidden;
  }
  .poster-inner {
    position: relative;
    width: 100%;
    height: 100%;
    border-radius: 10px;
    overflow: hidden;
    background: linear-gradient(180deg, var(--sky) 0%, var(--sky-deep) 70%);
  }
  .backdrop { position: absolute; inset: 0; width: 100%; height: 100%; }
  .bride-portrait {
    position: absolute;
    left: 460px; top: 0;
    width: 327px; height: 330px;
    background: radial-gradient(ellipse at 55% 45%, #8cc3e6 0%, var(--photo-bride) 55%, rgba(47,143,196,0) 85%);
  }
  .couple-photo {
    position: absolute;
    left: 20px; top: 110px;
    width: 510px; height: 880px;
    border-radius: 40% 40% 12% 12%;
    background: linear-gradient(180deg, #4a3b36 0%, var(--photo-couple) 40%, #c99a3a 62%, #6e4a32 100%);
    opacity: 0.92;
  }
  .title {
    position: absolute;
    left: 95px; top: 95px;
    width: 620px;
    font-family: "Yellowtail", cursive;
    color: var(--title);
    -webkit-text-stroke: 2px var(--ink);
    line-height: 0.95;
  }
  .title span { display: block; }
  .title .line-1 { font-size: 118px; transform: rotate(-4deg); }
  .title .line-2 { font-size: 92px; margin-left: 340px; margin-top: -10px; }
  .title .line-3 { font-size: 118px; margin-left: 300px; margin-top: -8px; }
  .billing {
    position: absolute;
    left: 60px; top: 1000px;
    width: 690px;
    display: flex;
    align-items: center;
    justify-content: space-between;
    font-family: "Yellowtail", cursive;
    color: var(--title);
  }
  .star-name {
    position: relative;
    width: 230px;
    font-size: 38px;
    line-height: 0.9;
    text-align: center;
    -webkit-text-stroke: 1px var(--ink);
  }
  .star-name::before {
    content: "";
    position: absolute;
    left: 0; right: 0; top: 50%;
    height: 34px;
    transform: translateY(-50%) rotate(-3deg);
    background: var(--stroke-blue);
    border-radius: 18px;
    opacity: 0.85;
    z-index: -1;
  }
  .star-name { z-index: 1; isolation: isolate; }
  .ampersand {
    font-family: "Kaushan Script", cursive;
    font-size: 64px;
    color: #ffffff;
    -webkit-text-stroke: 2px var(--ink);
  }
  .presenter {
    position: absolute;
    left: 0; right: 0; top: 1085px;
    text-align: center;
    font-family: "Kaushan Script", cursive;
    font-size: 36px;
    color: var(--ink);
  }
</style>
</head>
<body>
  <main class="poster">
    <div class="poster-inner">
      <svg class="backdrop" viewBox="0 0 787 1176" preserveAspectRatio="none" aria-hidden="true">
        <defs>
          <radialGradient id="sunGlow" cx="0.5" cy="0.5" r="0.5">
            <stop offset="0" stop-color="#e5302e"/>
            <stop offset="0.8" stop-color="#d81f26"/>
            <stop offset="1" stop-color="#a9151c"/>
          </radialGradient>
          <linearGradient id="goldBand" x1="0" y1="0" x2="0" y2="1">
            <stop offset="0" stop-color="#f7bd3c"/>
            <stop offset="1" stop-color="#f2ab27"/>
          </linearGradient>
        </defs>
        <circle class="sun" cx="395" cy="620" r="305" fill="url(#sunGlow)"/>
        <path class="ground-edge" d="M0,880 Q380,790 787,700 L787,1176 L0,1176 Z" fill="#d99419"/>
        <path class="ground" d="M0,895 Q380,805 787,716 L787,1176 L0,1176 Z" fill="url(#goldBand)"/>
      </svg>

      <div class="bride-portrait" role="img" aria-label="Soft blue-tinted portrait of the bride in profile"></div>
      <div class="couple-photo" role="img" aria-label="Groom carrying the bride in his arms, she in a yellow coat and tall brown boots"></div>

      <h1 class="title">
        <span class="line-1">The Wedding</span>
        <span class="line-2">of the</span>
        <span class="line-3">Year</span>
      </h1>

      <div class="billing">
        <p class="star-name">Marla Quenstedder</p>
        <span class="ampersand">&amp;</span>
        <p class="star-name">Daniel Fenwoller</p>
      </div>

      <p class="presenter">Presented by Pell Arrow Studios</p>
    </div>
  </main>
</body>
</html>
```